We specialize in pizza, pasta and salads and are now offering TAKE & BAKE and GRAB & GO ...

Looking for either a 8.5" x 11" or similar for a instore display. WILL BE ON A SWIVELING HOLDER to catch customers attention.

**THIS IS A DOUBLE SIDED PRINT**

ONE SIDE will consist of WHAT'S FOR DINNER TONIGHT? and the following:
* Take & Bake"
* "Baked Pasta"
* Freshly made in house
* Lasagna
$13.50
- please include attached closeup picture and logo

THE OTHER SIDE will consist of
mini charcutier board.
* snack size charcutier delight *
* Enjoy the flavors of gourmet snacking, all in one convenient box!

PRICE $8.99

Winning design will be commissioned to design labels for "grab and go" for take and bake pasta, charcuterie box, pasta salads, candy etc.

Thank you and please do not hesitate to ask any questions.

www.calderipizza.ca
www.fernloop.ca
Logo to be interchanged as they are affiliated meaning FernLoop is a brand within Calderi pizza.

Target Market(s)

our target market is customers who have already entered our business. This is to upsel

Industry/Entity Type

We are in a self serve enviroment and target business people

Requirements
Must have
• must be clean and catchy. We are located in a professional business community.
Nice to have
• Must be appealing, appetizing and utilize our website colors
Should not have
• should not have any carton drawings and not be cluttered (busy)

```html
<!DOCTYPE html>
<html lang="en">
<head>
<meta charset="utf-8">
<title>Take &amp; Bake – Baked Pasta &amp; Lasagna</title>
<link href="https://fonts.googleapis.com/css2?family=Kaushan+Script&family=Montserrat:wght@300;400;700;800;900&display=swap" rel="stylesheet">
<style>
  :root{
    --wine:#8a1a20;
    --brick:#b22a33;
    --white:#ffffff;
    --yellow:#f6ee1a;
    --green:#16b31a;
    --orange:#e8620e;
    --orange-dark:#c9410c;
    --ink:#26304a;
    --grey:#3a3a3a;
  }
  *{margin:0;padding:0;box-sizing:border-box}
  html,body{width:972px;height:1200px;overflow:hidden;background:var(--white)}
  .poster{position:relative;width:972px;height:1200px;overflow:hidden;background:var(--white);font-family:"Montserrat",sans-serif}
  .backdrop{position:absolute;inset:0;width:972px;height:1200px}
  .kicker{position:absolute;top:62px;left:0;width:100%;text-align:center;color:var(--yellow);font-weight:900;font-size:35px;letter-spacing:2.5px}
  .script{font-family:"Kaushan Script",cursive;color:var(--white);position:absolute;white-space:nowrap;line-height:1;font-weight:400}
  .title-word{top:128px;font-size:205px;transform-origin:left top;transform:scaleX(.84)}
  .title-take{left:80px}
  .title-bake{left:505px}
  .title-amp{left:432px;top:205px;font-size:84px}
  .subtitle{top:368px;left:395px;font-size:98px;transform-origin:left top;transform:scaleX(.92)}
  .photo{position:absolute}
  .photo-pasta{left:95px;top:405px;width:630px;height:205px;border-radius:40px 60px 90px 90px;
    background:radial-gradient(ellipse at 50% 45%,#f4e6c8 0%,#e9c48a 45%,#c8672e 80%,#b7d6dc 100%);transform:skewX(-8deg)}
  .photo-lasagna{left:88px;top:566px;width:790px;height:336px;border-radius:50%;
    background:radial-gradient(ellipse at 50% 45%,#f2cf7a 0%,#d98a3c 35%,#c2502a 55%,#efe9dc 72%,#f7f4ec 100%)}
  .price{position:absolute;left:72px;top:605px;width:164px;height:160px;border-radius:50%;
    background:linear-gradient(180deg,var(--orange),var(--orange-dark));border:6px solid #b83a0e;box-shadow:inset 0 0 0 3px rgba(255,255,255,.9);
    color:var(--white);display:flex;align-items:center;justify-content:center;font-weight:800}
  .price .cur{font-size:24px;align-self:flex-start;margin-top:46px}
  .price .whole{font-size:64px;letter-spacing:-3px;line-height:1;transform:scaleX(.8);margin:0 -4px}
  .price .cents{font-size:24px;align-self:flex-start;margin-top:46px}
  .badge{position:absolute;left:697px;top:567px;width:198px;height:198px}
  .lasagna{position:absolute;top:772px;left:162px;font-family:"Kaushan Script",cursive;color:var(--brick);font-size:205px;line-height:1;letter-spacing:-4px;white-space:nowrap}
  .brands{position:absolute;top:1050px;left:0;width:100%;height:100px}
  .brand{position:absolute;display:flex;flex-direction:column;align-items:center;gap:6px;color:var(--ink);font-weight:700;font-size:22px}
  .brand-loop{left:260px;top:0;width:140px}
  .brand-dot{width:62px;height:62px;border-radius:50%;border:3px solid var(--ink)}
  .brand-name{position:absolute;left:488px;top:38px;font-weight:300;font-size:38px;color:var(--grey);letter-spacing:1px}
</style>
</head>
<body>
<main class="poster">
  <svg class="backdrop" viewBox="0 0 972 1200" aria-hidden="true">
    <rect width="972" height="820" fill="var(--brick)"/>
    <path fill="var(--wine)" d="M0 0H972V388
      L964 384 L958 390 L950 379 L941 383 L934 372 L925 376 L918 364 L909 368 L902 356 L894 358 L888 345 L879 349 L872 336 L864 338 L857 326 L848 329 L840 318 L830 320 L822 309 L812 312 L804 300 L794 303 L786 292 L776 295 L768 284 L756 287 L748 277 L736 280 L726 270 L714 273 L704 264 L690 267 L680 259 L666 262 L654 255 L640 258 L628 252 L612 256 L600 250 L584 255 L572 250 L556 256 L545 252 L530 259 L518 257 L505 265 L494 262 L482 272 L470 270 L458 280 L446 279 L434 289 L421 287 L410 297 L397 296 L386 305 L372 304 L360 312 L346 311 L334 319 L318 318 L306 326 L290 324 L278 332 L262 331 L250 339 L234 337 L222 345 L206 343 L194 350 L178 349 L166 356 L150 354 L138 361 L122 359 L110 366 L94 364 L82 371 L66 369 L54 376 L38 374 L26 381 L12 379 L0 386Z"/>
    <path fill="var(--white)" d="M0 642
      L8 648 L14 640 L20 652 L28 647 L33 660 L42 656 L46 670 L55 668 L58 683 L68 681 L70 697 L80 702 L84 720 L95 728 L100 748 L112 755 L120 772 L134 780 L145 795 L162 800 L180 812 L220 822 L300 832 L420 842 L560 845 L700 838 L790 826 L812 812 L826 804 L838 793 L850 786 L860 773 L872 768 L880 754 L892 750 L898 736 L910 733 L914 718 L926 716 L930 702 L941 700 L945 688 L955 687 L958 675 L966 674 L972 664 V1200 H0Z"/>
    <g fill="var(--wine)">
      <circle cx="930" cy="405" r="3"/><circle cx="948" cy="398" r="2"/><circle cx="908" cy="392" r="2.5"/>
      <circle cx="60" cy="392" r="2.5"/><circle cx="30" cy="398" r="2"/>
    </g>
    <g fill="var(--brick)">
      <circle cx="18" cy="662" r="3"/><circle cx="40" cy="684" r="2.5"/><circle cx="952" cy="700" r="3"/><circle cx="930" cy="724" r="2.5"/>
    </g>
  </svg>

  <p class="kicker">WHAT'S FOR DINNER TONIGHT?</p>
  <h1>
    <span class="script title-word title-take">Take</span>
    <span class="script title-amp">&amp;</span>
    <span class="script title-word title-bake">Bake</span>
  </h1>

  <div class="photo photo-pasta" role="img" aria-label="Baked rigatoni pasta with meat sauce and melted cheese in a glass dish"></div>
  <div class="photo photo-lasagna" role="img" aria-label="Slice of meat lasagna topped with basil on a white plate with a fork"></div>

  <h2 class="script subtitle">Baked Pasta</h2>

  <div class="price"><span class="cur">$</span><span class="whole">13</span><span class="cents">.50</span></div>

  <svg class="badge" viewBox="0 0 198 198">
    <circle cx="99" cy="99" r="97" fill="var(--green)"/>
    <circle cx="99" cy="99" r="64" fill="#c99a55" role="img" aria-label="Close-up of lasagna with stretching cheese on a fork"/>
    <defs><path id="badgeArc" d="M99 99 m-75 0 a75 75 0 1 1 150 0 a75 75 0 1 1 -150 0"/></defs>
    <text fill="var(--white)" font-family="Montserrat, sans-serif" font-weight="800" font-size="21" letter-spacing="1.5">
      <textPath href="#badgeArc" startOffset="8">FRESHLY MADE IN HOUSE</textPath>
    </text>
  </svg>

  <h2 class="lasagna">Lasagna</h2>

  <footer class="brands">
    <div class="brand brand-loop"><span class="brand-dot"></span>FernLoop</div>
    <div class="brand-name">Calderi pizza</div>
  </footer>
</main>
</body>
</html>
```